Business and Success Coaching Business Card

Need a business card for my coaching business. I coach small businesses, career professionals and, individuals wanting to unlock their human potential and achieve excellence. At the heart of our methodology is the Shaping Purposeful Action Routines Knowingly (SPARK) approach to formulate empowerment, create principles for success and setting achievable outcomes. I would like something that incorporates our new logo, something clean and sharp with a solid darker, but complementary background, color on the card front. The back should be white where there will be room for three questions

Target Market(s)

People looking to advance and improve themselves through a success coach

Industry/Entity Type

Life Coaching

Contact Information for Business Card

Contact information on card.
Business name on front of card
Questions on back

Font styles to use
Other font styles liked:
• Century Gothic or other Serif style fonts that look similar to Century Gothic

Colors

Designer to choose colors to be used in the design.

Requirements
Must have
• Logo on front of card
• Business name - The Steady Forge
• Contact name - Ted Harlow
• Address - Box 4619, Littleton, CO 80127-4619
• Phone number - 303-555-0147
• Email address - harlow.ted@thesteadyforge.example
• Certifications - CSC, CCHt, PTT, PNLP
• Back of card
• Three questions on the back of the card:
• If you were at your best, what would you do right now?
• What is the decision you have been avoiding?
• What's one action you could take in the next 10 minutes?
Nice to have
• I would like to see a solid color on the front of the card that compliments the logo.
• Back should be white, or could be contrasting, but need to have the three questions.

```html
<!DOCTYPE html>
<html lang="en">
<head>
<meta charset="utf-8">
<title>The Steady Forge – Business Card</title>
<link rel="stylesheet" href="https://fonts.googleapis.com/css2?family=Questrial&family=Mulish:wght@400;600;700&display=swap">
<style>
  :root {
    --stage: #e4e4e2;
    --navy-deep: #0b1a3d;
    --navy-band: #22386e;
    --accent-blue: #4a86c8;
    --ray-pale: #c9d6ea;
    --ink-navy: #1f3474;
    --paper: #ffffff;
    --faint: #eceef4;
    --text-light: #f2f4f8;
  }
  * { box-sizing: border-box; margin: 0; padding: 0; }
  html, body { width: 1200px; height: 850px; overflow: hidden; }
  body {
    background: var(--stage);
    font-family: "Questrial", "Mulish", sans-serif;
    position: relative;
  }
  .card {
    position: absolute;
    width: 560px;
    height: 320px;
    top: 265px;
    overflow: hidden;
    box-shadow: 0 6px 18px rgba(0,0,0,0.18);
  }

  /* Back of card */
  .card-back { left: 27px; background: var(--paper); }
  .back-decoration {
    position: absolute;
    right: 0; top: 0;
    width: 240px; height: 320px;
    background: linear-gradient(160deg, var(--paper) 10%, var(--faint) 55%, var(--paper) 95%);
  }
  .questions {
    position: absolute;
    left: 40px; top: 34px;
    width: 470px;
    color: var(--ink-navy);
  }
  .questions-title {
    text-align: center;
    font-family: "Mulish", sans-serif;
    font-weight: 700;
    font-size: 22px;
    letter-spacing: 0.5px;
    margin-bottom: 26px;
  }
  .question {
    font-family: "Mulish", sans-serif;
    font-size: 15px;
    padding-bottom: 22px;
    border-bottom: 2px dotted var(--ink-navy);
    margin-bottom: 22px;
  }

  /* Front of card */
  .card-front { left: 613px; background: var(--navy-deep); }
  .front-shapes { position: absolute; inset: 0; }
  .logo-art {
    position: absolute;
    left: 330px; top: 18px;
    width: 210px; height: 180px;
    border-radius: 50% 50% 8px 8px;
    background: radial-gradient(ellipse at 50% 45%, var(--accent-blue) 0%, #2d5a99 45%, var(--navy-deep) 80%);
    opacity: 0.9;
  }
  .brand {
    position: absolute;
    left: 32px; top: 98px;
  }
  .brand-name {
    font-size: 27px;
    color: var(--accent-blue);
    letter-spacing: 0.3px;
  }
  .brand-tagline {
    font-size: 14px;
    color: var(--accent-blue);
    margin-top: 2px;
    letter-spacing: 0.5px;
  }
  .person {
    position: absolute;
    left: 32px; top: 176px;
  }
  .person-name {
    font-family: "Mulish", sans-serif;
    font-weight: 700;
    font-size: 24px;
    color: var(--accent-blue);
  }
  .person-credentials {
    font-size: 14px;
    color: var(--text-light);
    margin-top: 4px;
    letter-spacing: 0.4px;
  }
  .contact-list {
    position: absolute;
    left: 32px; top: 248px;
    list-style: none;
  }
  .contact-item {
    display: flex;
    align-items: center;
    gap: 10px;
    font-size: 13px;
    color: var(--text-light);
    line-height: 21px;
    letter-spacing: 0.3px;
  }
  .contact-icon { width: 12px; height: 12px; flex: none; }
  .address {
    position: absolute;
    right: 22px; top: 214px;
    width: 230px;
    text-align: center;
    color: var(--text-light);
    font-size: 13px;
    letter-spacing: 0.3px;
  }
  .address svg { display: block; margin: 0 auto 6px; }
</style>
</head>
<body>

  <section class="card card-back" aria-label="Back of card">
    <div class="back-decoration" role="img" aria-label="Faint brand emblem area"></div>
    <div class="questions">
      <h2 class="questions-title">Questions for you?</h2>
      <p class="question">1. If you were at your best, what would you do right now?</p>
      <p class="question">2. What is the decision you have been avoiding?</p>
      <p class="question">3. What's one action you could take in the next 10 minutes?</p>
    </div>
  </section>

  <section class="card card-front" aria-label="Front of card">
    <svg class="front-shapes" width="560" height="320" viewBox="0 0 560 320" aria-hidden="true">
      <path d="M250 320 C300 300 330 250 350 215 C380 180 420 185 460 182 C510 178 540 190 560 200 L560 320 Z" fill="var(--navy-band)"/>
    </svg>
    <div class="logo-art" role="img" aria-label="Brand emblem area"></div>

    <div class="brand">
      <div class="brand-name">The Steady Forge</div>
      <div class="brand-tagline">Start your next phase</div>
    </div>

    <div class="person">
      <div class="person-name">Ted Harlow</div>
      <div class="person-credentials">CSC, CCHt, PTT, PNLP</div>
    </div>

    <ul class="contact-list">
      <li class="contact-item">
        <svg class="contact-icon" viewBox="0 0 12 12"><path d="M2.5 1 L4.5 1 L5.2 3.6 L4 4.6 C4.6 6 5.8 7.3 7.4 8 L8.4 6.8 L11 7.5 L11 9.5 C11 10.3 10.3 11 9.5 11 C5 10.5 1.5 7 1 2.5 C1 1.7 1.7 1 2.5 1 Z" fill="var(--accent-blue)"/></svg>
        303-555-0147
      </li>
      <li class="contact-item">
        <svg class="contact-icon" viewBox="0 0 12 12"><rect x="0.5" y="2" width="11" height="8" fill="var(--accent-blue)"/><path d="M0.5 2 L6 6.5 L11.5 2" fill="none" stroke="var(--navy-deep)" stroke-width="1"/></svg>
        harlow.ted@thesteadyforge.example
      </li>
      <li class="contact-item">
        <svg class="contact-icon" viewBox="0 0 12 12"><circle cx="6" cy="6" r="5.3" fill="var(--accent-blue)"/><path d="M0.7 6 H11.3 M6 0.7 C3.5 3.5 3.5 8.5 6 11.3 M6 0.7 C8.5 3.5 8.5 8.5 6 11.3" fill="none" stroke="var(--navy-deep)" stroke-width="0.8"/></svg>
        www.thesteadyforge.example
      </li>
    </ul>

    <div class="address">
      <svg width="14" height="16" viewBox="0 0 14 16" aria-hidden="true"><path d="M7 1 C4 1 2 3.2 2 5.8 C2 9 7 13 7 13 C7 13 12 9 12 5.8 C12 3.2 10 1 7 1 Z" fill="none" stroke="var(--accent-blue)" stroke-width="1.4"/><circle cx="7" cy="5.8" r="1.8" fill="var(--accent-blue)"/><path d="M2 15 H12" stroke="var(--accent-blue)" stroke-width="1.2"/></svg>
      Box 4619, Littleton, CO 80127-4619
    </div>
  </section>

</body>
</html>
```